Velvet Pressings Techno Label Business Card

I'm looking for a very clean business card for my Velvet Pressings music label. The label focusses on techno music. The card should include:

• my name : Bram Quintel as "Founder & CEO"
• email address: bram@velvet-pressings.example
• web: www.velvet-pressings.example
• facebook logo + /velvetpress
• twitter logo + /velvetpress
• soundcloud logo + /velvetpressings

Feel free to include your ideas! I'm looking forward to discuss about it.

Bram

Industry/Entity Type

Business

Contact Information for Business Card

I don't like glossy cards. Prefer matt.

Requirements
Nice to have
• Maybe on one side the complete logo, other side just the icon.
Should not have
• Flashy stuff. Must be clean and business like style.

```html
<!DOCTYPE html>
<html lang="en">
<head>
<meta charset="utf-8">
<title>Velvet Pressings – Business Card</title>
<link rel="stylesheet" href="https://fonts.googleapis.com/css2?family=Roboto:wght@300;400;700&display=swap">
<style>
  :root {
    --bg-top: #202020;
    --bg-bottom: #101010;
    --card: #2f3033;
    --card-edge: #3a3b3e;
    --orange: #d8691c;
    --grey-band: #77787b;
    --grey-text: #9a9b9e;
    --light-text: #c9cacc;
    --white: #f2f2f2;
    --divider: #45464a;
    --dot: #5a5b5f;
  }
  * { box-sizing: border-box; margin: 0; padding: 0; }
  html, body { width: 1200px; height: 900px; overflow: hidden; }
  body {
    background: radial-gradient(ellipse at 50% 35%, var(--bg-top), var(--bg-bottom) 75%);
    font-family: "Roboto", Arial, sans-serif;
    display: flex;
    align-items: center;
    justify-content: center;
    gap: 30px;
  }
  .card {
    position: relative;
    width: 560px;
    height: 310px;
    background: var(--card);
    border: 1px solid var(--card-edge);
    box-shadow: 0 30px 60px rgba(0,0,0,.55);
    overflow: hidden;
  }

  /* Front */
  .brand {
    position: absolute;
    left: 40px;
    top: 70px;
    display: flex;
    align-items: center;
    gap: 16px;
  }
  .brand-square {
    width: 22px;
    height: 22px;
    background: var(--orange);
  }
  .brand-name {
    font-size: 36px;
    font-weight: 400;
    color: var(--grey-text);
    letter-spacing: -0.5px;
  }
  .title-band {
    position: absolute;
    right: 0;
    top: 168px;
    width: 300px;
    height: 52px;
    background: var(--grey-band);
    display: flex;
    align-items: center;
    justify-content: flex-end;
    padding-right: 22px;
  }
  .title-band span {
    color: var(--light-text);
    font-size: 15px;
    font-weight: 300;
  }
  .name-band {
    position: absolute;
    left: 0;
    top: 184px;
    width: 300px;
    height: 60px;
    background: var(--orange);
    clip-path: polygon(0 0, 100% 0, 86% 100%, 0 100%);
    display: flex;
    align-items: center;
    padding-left: 92px;
  }
  .person {
    color: var(--white);
    font-size: 22px;
    font-weight: 300;
  }
  .person strong { font-weight: 700; }
  .email {
    position: absolute;
    left: 0;
    bottom: 0;
    width: 270px;
    height: 66px;
    display: flex;
    align-items: center;
    gap: 12px;
    padding-left: 28px;
    color: var(--light-text);
    font-size: 13px;
    font-weight: 300;
    white-space: nowrap;
  }
  .email svg { width: 22px; height: 16px; flex: none; }
  .social {
    position: absolute;
    right: 0;
    bottom: 0;
    width: 300px;
    height: 66px;
    display: flex;
  }
  .social-item {
    flex: 1;
    display: flex;
    flex-direction: column;
    align-items: center;
    justify-content: center;
    gap: 7px;
    border-left: 1px solid var(--divider);
  }
  .social-dot {
    width: 16px;
    height: 16px;
    border-radius: 50%;
    background: var(--dot);
  }
  .social-handle {
    color: var(--grey-text);
    font-size: 11px;
    font-weight: 300;
    white-space: nowrap;
  }

  /* Back */
  .back-brand {
    position: absolute;
    left: 0;
    right: 0;
    top: 96px;
    display: flex;
    align-items: center;
    justify-content: center;
    gap: 16px;
  }
  .back-brand .brand-square { width: 26px; height: 26px; }
  .back-brand span {
    color: var(--grey-text);
    font-size: 38px;
    font-weight: 400;
    letter-spacing: -0.5px;
  }
  .website {
    position: absolute;
    left: 40px;
    bottom: 40px;
    width: 320px;
    padding-bottom: 10px;
    border-bottom: 1px solid var(--divider);
    color: var(--grey-text);
    font-size: 18px;
    font-weight: 400;
    white-space: nowrap;
  }
  .website strong { color: var(--orange); font-weight: 700; }
</style>
</head>
<body>
  <section class="card card-front" aria-label="Business card front">
    <div class="brand">
      <span class="brand-square" aria-hidden="true"></span>
      <span class="brand-name">Velvet Pressings</span>
    </div>

    <div class="title-band"><span>Founder &amp; CEO</span></div>
    <div class="name-band">
      <p class="person"><strong>Bram</strong> Quintel</p>
    </div>

    <p class="email">
      <svg viewBox="0 0 22 16" aria-hidden="true">
        <rect x="0" y="0" width="22" height="16" fill="var(--light-text)"/>
        <path d="M0 0 L11 9 L22 0" fill="none" stroke="var(--card)" stroke-width="1.6"/>
      </svg>
      bram@velvet-pressings.example
    </p>

    <ul class="social" aria-label="Social profiles" style="list-style:none">
      <li class="social-item"><span class="social-dot"></span><span class="social-handle">/velvetpress</span></li>
      <li class="social-item"><span class="social-dot"></span><span class="social-handle">/velvetpress</span></li>
      <li class="social-item"><span class="social-dot"></span><span class="social-handle">/velvetpressings</span></li>
    </ul>
  </section>

  <section class="card card-back" aria-label="Business card back">
    <div class="back-brand">
      <span class="brand-square" aria-hidden="true"></span>
      <span>Velvet Pressings</span>
    </div>
    <p class="website">www.<strong>velvet-pressings</strong>.example</p>
  </section>
</body>
</html>
```